Kessel Fahrwerkstatt
Sehr angenehme zusammenarbeit nicht aufdringlich und genau auf die Wünsche eingegangen. Wir werde sicher noch mehr zusammen Arbeiten. Gruss Lukas Hemmerle Inhaber Kessel Fahrwerkstatt
Zielgruppe
Dinks und Kunden mit viel Erfolg und hohem Ausgabepotential.
Aufgabenstellung
Unsere Firma vertreibt Fahrzeuge im Luxusbereich hauptgebiet Valtro aber auch andere Sportwagen. Was uns fehlt ist ein optischer Wiedererkennugswert. Deshalb hätten wir gerne ein Visitenkarten Design und Briefpapier Design. Später soll auch noch eine Webseite mit gleichem Wiedererkennungswert entstehen. " Roter Faden "

```html
<!DOCTYPE html>
<html lang="de">
<head>
<meta charset="utf-8">
<title>Kessel Fahrwerkstatt – Visitenkarte und Briefpapier</title>
<link rel="stylesheet" href="https://fonts.googleapis.com/css2?family=Source+Sans+3:wght@400;600;700&family=Source+Serif+4:wght@400&display=swap">
<style>
  :root {
    --paper: #ffffff;
    --ink: #111111;
    --sphere-dark: #050505;
    --sphere-mid: #2b2b2b;
    --sphere-rim: #5a5a5a;
    --silver-light: #f2f3f4;
    --silver-mid: #c9cdd0;
    --silver-dark: #9ea5a8;
    --sage: #7f8f80;
    --sage-dark: #5c665e;
    --band: #ece7d6;
    --shadow: rgba(0,0,0,0.55);
    --page-line: #8a8a8a;
    --text-font: "Source Sans 3", sans-serif;
    --footer-font: "Source Serif 4", serif;
  }
  * { margin: 0; padding: 0; box-sizing: border-box; }
  html, body { width: 1200px; height: 848px; overflow: hidden; background: var(--paper); }
  body { position: relative; font-family: var(--text-font); color: var(--ink); }

  .sphere {
    position: absolute; border-radius: 50%;
    background: radial-gradient(circle at 50% 40%, var(--sphere-mid) 0%, var(--sphere-dark) 55%, var(--sphere-dark) 85%, var(--sphere-rim) 100%);
  }

  /* business card – front */
  .card { position: absolute; width: 242px; height: 154px; overflow: hidden; box-shadow: 6px 7px 4px var(--shadow); }
  .card--front { left: 163px; top: 145px; }
  .card--front .backdrop-top {
    position: absolute; inset: 0 0 auto 0; height: 48px;
    background: linear-gradient(90deg, var(--silver-light), #e4e7ea 60%, var(--silver-mid));
  }
  .card--front .backdrop-photo {
    position: absolute; left: 0; right: 0; top: 67px; bottom: 0;
    background: linear-gradient(100deg, var(--sage-dark), var(--sage) 30%, #a9b1ac 55%, var(--sage-dark));
  }
  .card--front .name-band {
    position: absolute; left: 0; right: 0; top: 47px; height: 20px;
    background: linear-gradient(90deg, #f7f4ea, var(--band));
  }
  .card--front .sphere { width: 190px; height: 190px; left: 108px; top: 78px; }
  .card .wordmark { position: absolute; font-weight: 400; color: var(--ink); white-space: nowrap; }
  .card--front .wordmark { left: 50px; top: 16px; font-size: 11.5px; }
  .card .person { position: absolute; right: 8px; top: 50px; font-size: 9.5px; font-weight: 700; }
  .card .contact {
    position: absolute; right: 7px; top: 80px; text-align: right;
    color: #fff; font-size: 7px; line-height: 9.1px; font-weight: 600;
  }
  .card .contact .plain { font-weight: 400; }

  /* business card – back */
  .card--back { left: 237px; top: 359px; }
  .card--back .backdrop-photo {
    position: absolute; inset: 0 0 auto 0; height: 78px;
    background: linear-gradient(90deg, #a7aca9, #8e9a8f 40%, #6f7d72 70%, #b9c0bb);
  }
  .card--back .backdrop-silver {
    position: absolute; left: 0; right: 0; top: 78px; bottom: 0;
    background: linear-gradient(180deg, #eef0f1, #d9dcde 50%, var(--silver-dark));
  }
  .card--back .rule { position: absolute; background: rgba(120,120,120,0.45); }
  .card--back .rule--h { left: 70px; right: 0; top: 124px; height: 1px; }
  .card--back .rule--v { left: 70px; top: 100px; width: 1px; height: 54px; }
  .card--back .sphere { width: 170px; height: 170px; left: 105px; top: -48px; }
  .card--back .wordmark { left: 42px; top: 94px; font-size: 8px; font-weight: 700; }

  /* letterhead */
  .letter {
    position: absolute; left: 596px; top: 0; width: 596px; height: 843px;
    border-left: 1px solid var(--page-line); border-bottom: 1px solid var(--page-line);
    overflow: hidden; background: var(--paper);
  }
  .letter .sphere { width: 84px; height: 84px; left: -42px; top: 164px; }
  .letter .wordmark { position: absolute; left: 72px; top: 39px; font-size: 12px; }
  .letter .sender-line { position: absolute; left: 99px; top: 126px; font-size: 4.6px; font-weight: 700; }
  .letter .recipient { position: absolute; left: 99px; top: 140px; font-size: 9.6px; line-height: 11.9px; }
  .letter .content { position: absolute; left: 99px; top: 253px; width: 436px; font-size: 9.1px; line-height: 11.8px; }
  .letter .content p { margin-bottom: 8.3px; }
  .letter .signature { margin-top: 30px; padding-left: 2px; }
  .letter .footer {
    position: absolute; left: 38px; right: 40px; top: 793px;
    font-family: var(--footer-font); font-size: 5.6px; text-align: center; white-space: nowrap;
  }
</style>
</head>
<body>

  <section class="card card--front" aria-label="Visitenkarte Vorderseite">
    <div class="backdrop-top"></div>
    <div class="backdrop-photo" role="img" aria-label="Unscharfes Fahrzeugfoto in Grün- und Grautönen"></div>
    <div class="name-band"></div>
    <div class="sphere"></div>
    <div class="wordmark">Kessel Fahrwerkstatt</div>
    <div class="person">Lukas Hemmerle</div>
    <div class="contact">
      +41 79 555 18 27<br>
      info@kessel-fahrwerk.ch<br>
      www.kessel-fahrwerk.ch<br>
      <span class="plain">Büro : Werkhofweg 14<br>CH 8175 Lindenau<br>Showroom : Talackerstrasse 3<br>CH 8641 Rebwil</span>
    </div>
  </section>

  <section class="card card--back" aria-label="Visitenkarte Rückseite">
    <div class="backdrop-photo" role="img" aria-label="Unscharfes Fahrzeugfoto in Grau- und Grüntönen"></div>
    <div class="backdrop-silver"></div>
    <div class="rule rule--h"></div>
    <div class="rule rule--v"></div>
    <div class="sphere"></div>
    <div class="wordmark">Kessel Fahrwerkstatt</div>
  </section>

  <section class="letter" aria-label="Briefpapier">
    <div class="sphere"></div>
    <div class="wordmark">Kessel Fahrwerkstatt</div>
    <div class="sender-line">Name, Strasse, Postleitzahl Ort</div>
    <address class="recipient" style="font-style:normal">
      Kundenname<br>Abteilung<br>Firmenname<br>Anywhere Straße 52<br>23094 Irgendwostadt<br>Land
    </address>
    <div class="content">
      <p>Sehr geehrter Name,</p>
      <p>Andipsum dipsum nostis nulpute magnissis niatie te molor adignis sequips uscipisit, sit vel ipsuscing ent lut lan ulla feugait augueraesto odolore doluptatio cons dolor sismodo luptatuero do od dolore magnim dolor auguero eu facilis ea core estrud eugiat velis ad tat dio odolor augue magna corting eugait enim venibh et, quatumsan hendre tincinisi tisisl dolute moloreet atem velesequat alit aliquat, vel dolore faciduis dolore dignis dolorper il eugiamconsed deliquamcon henis alis atum duis at.</p>
      <p>Bore del ute faccum vercill aorper sent alit, venis autet, quipsustio eugue vero dolore velendre euis nos nonse dolessim illa feum dolor sumsan ectet lortincin vulputat amet, qui esto conulput acil in eugait vel essequam zzriusto diam, velit wissit autat.</p>
      <p>Obore dolor incip ea conummy nulput vel ullan henisim am in ute erciliqui ex ent et, quis augiat, commod tis enis num delit laor acing elis dolorer se eugue feu facinci liquis aut lut nulluptat er sum zzrit vulla consequis accum incidunt iusci blaortio odoloreet pratum veliquatie modit, quat. Ut nummodo exercilisl iriliqu ipsusto dolesequat. Ut wisl in ute consequam ad diam vulputpat lan hent vel doloreet utat ver si.</p>
      <p>Vullaorem iusci blamcon seniamcommy nit iureetum dolore con ea faccum iureet prat. In utat acidunt nullum venismolum ing exer iusci bla augue magna consequi tem veliquis nostion utpat.</p>
      <p>Nibh euipis esed ero doluptat. Ibh ex exeros exero dolesed dunt pratissi euis nismodipsum eu feugerit ipisl incilla faccum am init praese tat velis augue corem iriliqu amconsequat. Magnim ipit in ea acincil esto et wisl esenim volenit lorem del ut aut la commy nibh eui tiniam iure mod tem vel ipisit, quis nonsequi blan exerosto odolorem il irit num vel dolore et irit aute te dolestrud tin hent utet ut praestrud ea faccum venim venim il er iustion sequipsum quat.</p>
      <p>Do ea acilisis dolore min ercing endre consequat. Ero consequis ad euguerat, siscidunt laor sum iuscipis nullaoreet, velent ilit amconul laorperit lore diatum dui bla facipit irit alis ad dolorpe rostrud tem essequat praesequam, coreet ip er sim dit, velisim inciliquam, quis adigna feugue dolore et irillaor.</p>
      <p>Adiam zzrit,</p>
      <p class="signature">Veliquatin Veraessi</p>
    </div>
    <div class="footer">Kessel Fahrwerkstatt • Lukas Hemmerle • T +41 79 555 18 27 • info@kessel-fahrwerk.ch • www.kessel-fahrwerk.ch • Büro: Werkhofweg 14, CH-8175 Lindenau • Showroom: Talackerstr. 3, CH-8641 Rebwil</div>
  </section>

</body>
</html>
```